Tessaway Website Redesign

We have a web site called tessaway.com that is all about education/information about legal marijuana. We're looking to significantly improve the modern-ness and look/feel of the web site - and to make it look like many of the best web sites out there today.

The task will be to come up with a better design for:
- The home page: http://tessaway.com/
- The logo (see the logo at the top of each page)
- The header and footer (for all the pages)
- The vaporizer page: http://tessaway.com/collections/vaporizer
- The store map page: http://tessaway.com/pages/shop-marijuana-in-colorado-state

The output of the project will be:
- screenshots of the designs and any images needed
- PSD file

Key requirements:
- Style needs to look fresh/modern
- Especially on the vaporizers page, the key things we want to drive is conversion - getting more people to interact with the page and actually click on the links to purchase vaporizers

Note I clarified that I don't need code (HTML or CSS) for the project. I just need the designs, including images and the PSD file. Thanks.

Industry/Entity Type

Education

Font styles to use
Sans Serif

Requirements
Must have
• Must look like a modern/clean/fresh looking website design.

```html
<!DOCTYPE html>
<html lang="en">
<head>
<meta charset="utf-8">
<title>Tessaway – Shop marijuana in style</title>
<link rel="stylesheet" href="https://fonts.googleapis.com/css2?family=Arimo:wght@400;700&family=Open+Sans:wght@400;600;700&display=swap">
<style>
:root{
  --brand:#2a8ad6;
  --ink:#111;
  --muted:#555;
  --nav-active:#7fa8cf;
  --hero-top:#0a6ad6;
  --hero-bottom:#86bcec;
  --hero-edge:#1d5fae;
  --button:#3a8ee0;
  --band:#2f62a6;
  --footer:#f1f0ec;
  --star:#f2c200;
}
*{box-sizing:border-box;margin:0;padding:0}
html,body{width:762px;height:1200px;overflow:hidden;background:#fff}
body{position:relative;font-family:"Arimo",Arial,sans-serif;color:var(--ink)}
.abs{position:absolute}

/* header */
.logo{left:78px;top:18px;display:flex;align-items:flex-start;gap:6px}
.logo-dot{width:34px;height:34px;border-radius:50%;background:var(--brand);margin-top:3px}
.logo-name{font-size:37px;line-height:34px;color:var(--brand);letter-spacing:1px}
.logo-tag{font-size:11.5px;color:var(--brand);letter-spacing:1.6px;margin-top:1px}
.follow{left:612px;top:29px;width:80px;text-align:center;font-size:9px;font-weight:700;letter-spacing:.5px}
.follow-icons{display:flex;gap:11px;justify-content:center;margin-top:5px}
.sq{width:13px;height:13px;display:block}
.sq.one{background:#3b5a9e}.sq.two{background:#37a9e8}
.nav{left:0;top:72px;width:762px;height:27px}
.nav a{position:absolute;top:0;height:27px;line-height:27px;font-size:13.5px;font-weight:700;letter-spacing:1.3px;color:var(--ink);text-decoration:none}
.nav a.active{background:var(--nav-active);color:#fff;padding:0 6px;width:51px}
.caret{font-size:8px;margin-left:3px}

/* hero */
.hero{left:0;top:99px;width:762px;height:151px;background:linear-gradient(var(--hero-top) 0%,#1677dc 55%,var(--hero-bottom) 100%);border-bottom:2px solid var(--hero-edge);text-align:center;color:#fff}
.hero h1{font-size:30px;letter-spacing:2.5px;margin-top:45px}
.hero p{font-size:13px;font-weight:700;letter-spacing:1.5px;margin-top:14px}
.hero-arrow{top:76px;width:17px;height:17px}

/* articles */
.article{width:292px;height:80px}
.article-photo{left:0;top:0;width:73px;height:55px}
.article-title{left:78px;top:2px;width:212px;text-align:center;font-size:8.6px;line-height:11px}
.article-text{left:80px;top:24px;width:212px;font-size:5.7px;line-height:8px;color:#222}
.btn{right:0;top:62px;width:43px;height:14px;background:var(--button);color:#fff;font-size:5.5px;line-height:14px;text-align:center}

/* section headings */
.section-title{font-size:17px;font-weight:700;letter-spacing:1.6px}
.dash{height:5px;border-top:1px dashed #d3d3d3;border-bottom:1px dashed #d3d3d3}

/* products */
.band{left:0;top:645px;width:762px;height:158px;background:radial-gradient(ellipse at 40% 30%,#5f8fd0 0%,var(--band) 55%,#254f8c 100%)}
.product{top:16px;width:111px}
.product-photo{width:111px;height:94px;background:#fff;position:relative;overflow:hidden}
.product-shot{position:absolute;left:22px;top:12px;width:67px;height:74px;border-radius:6px}
.sale{position:absolute;right:0;top:0}
.price{color:#fff;font-size:7px;font-weight:700;text-align:center;margin-top:12px}
.stars{text-align:center;font-size:10px;line-height:10px;color:var(--star);letter-spacing:1px}
.stars .off{color:#fff}
.band-arrow{top:55px}

/* blog */
.author-photo{width:80px;height:80px;border-radius:50%;background:radial-gradient(circle,#c8c2ba,#7f7a74)}
.post-name{font-size:8px;font-weight:700}
.post-text{width:160px;font-size:6.4px;line-height:12.5px;font-weight:700;text-align:justify;margin-top:3px}

/* footer */
.footer{left:0;top:1022px;width:762px;height:178px;background:var(--footer);box-shadow:0 -3px 5px rgba(0,0,0,.08) inset}
.footer-map{left:0;top:0;width:762px;height:178px;background:linear-gradient(135deg,#f4f3ef,#e9e8e3 50%,#f3f2ee)}
.foot-col{font-family:"Open Sans",Arial,sans-serif;font-size:6.3px;line-height:11.3px;font-weight:600;color:#222}
.foot-col h3{font-size:8px;font-weight:600;margin-bottom:3px}
.social-row{display:flex;align-items:center;gap:8px;font-size:7px;margin-top:9px}
.legal{font-family:"Open Sans",Arial,sans-serif;font-size:4.5px;color:#222}
</style>
</head>
<body>

<header>
  <div class="abs logo">
    <span class="logo-dot"></span>
    <div><div class="logo-name">tessaway</div><div class="logo-tag">shop marijuana in style</div></div>
  </div>
  <div class="abs follow">Fallow us on
    <div class="follow-icons"><span class="sq one"></span><span class="sq two"></span></div>
  </div>
  <nav class="abs nav">
    <a class="active" href="#" style="left:77px">Home</a>
    <a href="#" style="left:187px">Blog</a>
    <a href="#" style="left:277px">Marijuna 101</a>
    <a href="#" style="left:432px">Legal Marijuna<span class="caret">▼</span></a>
    <a href="#" style="left:597px">Vaporizers<span class="caret">▼</span></a>
  </nav>
</header>

<section class="abs hero">
  <h1>Welcome To Tessaway</h1>
  <p>Shop marijuana in style</p>
  <svg class="abs hero-arrow" style="left:77px" viewBox="0 0 17 17"><circle cx="8.5" cy="8.5" r="7.5" fill="none" stroke="#cfe3f8" stroke-width="1"/><path d="M10 5 6.5 8.5 10 12" fill="none" stroke="#cfe3f8" stroke-width="1.3"/></svg>
  <svg class="abs hero-arrow" style="left:669px" viewBox="0 0 17 17"><circle cx="8.5" cy="8.5" r="7.5" fill="none" stroke="#cfe3f8" stroke-width="1"/><path d="M7 5 10.5 8.5 7 12" fill="none" stroke="#cfe3f8" stroke-width="1.3"/></svg>
</section>

<main>
  <article class="abs article" style="left:77px;top:274px">
    <div class="abs article-photo" role="img" aria-label="Hand holding a lit joint" style="background:linear-gradient(135deg,#5a4a44,#c9b7a8)"></div>
    <h2 class="abs article-title" style="font-weight:400">Denver Man Admits Smoking Weed Was More Fun When It Was Illegal</h2>
    <p class="abs article-text" style="top:32px">Owen Pellard, a marijuana enthusiast living in the Denver area, told reporters Wednesday that he enjoyed getting high more when it was illegal.</p>
    <span class="abs btn">View Details</span>
  </article>
  <article class="abs article" style="left:397px;top:274px">
    <div class="abs article-photo" role="img" aria-label="Stack of chocolate brownies" style="background:linear-gradient(135deg,#3b2116,#7a4a33)"></div>
    <h2 class="abs article-title" style="font-weight:400">The Best Ways To Take Marijuana (And Their Effects)</h2>
    <p class="abs article-text">There are many ways to get high and a lot of them have different effects. So here's our list of the best ways to get high and the different ways you'll feel it.</p>
    <span class="abs btn">View Details</span>
  </article>
  <article class="abs article" style="left:77px;top:386px">
    <div class="abs article-photo" role="img" aria-label="Cupped hands full of cannabis buds" style="background:linear-gradient(135deg,#c9b6a4,#6f7a4c)"></div>
    <h2 class="abs article-title" style="font-weight:400">Six Ways To Improve Your High</h2>
    <p class="abs article-text">Getting high on marijuana is wonderful, but there are a few little annoyances we all notice after we've done it a few times. Here's a six hacks to make your high as enjoyable and irritation free as possible.</p>
    <span class="abs btn">View Details</span>
  </article>
  <article class="abs article" style="left:397px;top:386px">
    <div class="abs article-photo" role="img" aria-label="Glass jar of cannabis held in hands" style="background:linear-gradient(135deg,#3f4a34,#b99a86)"></div>
    <h2 class="abs article-title" style="font-weight:400">The 6 Best Ways to Store Your Weed</h2>
    <p class="abs article-text">There's nothing worse than opening up your stash and finding out that your weed is completely dried out and stale. To help protect your weed and keep it fresh for longer, here are the best storage</p>
    <span class="abs btn">View Details</span>
  </article>
  <article class="abs article" style="left:77px;top:498px">
    <div class="abs article-photo" role="img" aria-label="Close-up of cannabis buds" style="background:linear-gradient(135deg,#eef0e6,#8c9a5a)"></div>
    <h2 class="abs article-title" style="font-weight:400">The States Most Likely To Legalize Weed Next</h2>
    <p class="abs article-text">If you live in the United States anywhere other than Colorado or Washington State then you're pretty screwed as far as legal marijuana goes. But never fear! Here are the states most likely to legalize weed next.</p>
    <span class="abs btn">View Details</span>
  </article>
  <article class="abs article" style="left:397px;top:498px">
    <div class="abs article-photo" role="img" aria-label="Person in orange sitting in a prison cell" style="background:linear-gradient(135deg,#2f2b2a,#a54a2e 60%,#d9d3cc)"></div>
    <h2 class="abs article-title" style="font-weight:400">Five Of The Most Unfair Marijuana Sentences</h2>
    <p class="abs article-text">In 48 states in America recreational marijuana use is still illegal. Over this time countless people have received completely over the top sentences for non-violent marijuana offences, but these five really are something else.</p>
    <span class="abs btn">View Details</span>
  </article>

  <h2 class="abs section-title" style="left:79px;top:611px">Vaporizers Products</h2>
  <div class="abs dash" style="left:282px;top:621px;width:404px"></div>

  <section class="abs band">
    <svg class="abs band-arrow" style="left:36px" width="14" height="24" viewBox="0 0 14 24"><path d="M12 1 2 12l10 11" fill="none" stroke="#fff" stroke-width="1.6"/></svg>
    <svg class="abs band-arrow" style="left:706px" width="14" height="24" viewBox="0 0 14 24"><path d="M2 1l10 11L2 23" fill="none" stroke="#fff" stroke-width="1.6"/></svg>

    <div class="abs product" style="left:76px">
      <div class="product-photo"><div class="product-shot" role="img" aria-label="Wooden box vaporizer" style="left:6px;top:18px;width:98px;height:62px;background:linear-gradient(135deg,#e4cf9c,#9c7f45)"></div>
        <svg class="sale" width="40" height="40" viewBox="0 0 40 40"><path d="M0 0h40v40z" fill="#000"/><text x="27" y="14" fill="#fff" font-size="7" font-family="Arimo,sans-serif" transform="rotate(45 27 14)" text-anchor="middle">SALE</text></svg></div>
      <div class="price">$119.00</div><div class="stars">★★★★<span class="off">★</span></div>
    </div>
    <div class="abs product" style="left:200px">
      <div class="product-photo"><div class="product-shot" role="img" aria-label="Desktop vaporizer with whip" style="background:linear-gradient(#bbb,#222)"></div>
        <svg class="sale" width="40" height="40" viewBox="0 0 40 40"><path d="M0 0h40v40z" fill="#000"/><text x="27" y="14" fill="#fff" font-size="7" font-family="Arimo,sans-serif" transform="rotate(45 27 14)" text-anchor="middle">SALE</text></svg></div>
      <div class="price">$239.00</div><div class="stars">★★★★★</div>
    </div>
    <div class="abs product" style="left:325px">
      <div class="product-photo"><div class="product-shot" role="img" aria-label="Cone-shaped steel vaporizer" style="left:14px;width:84px;background:linear-gradient(135deg,#e5e5e5,#6d6d6d)"></div>
        <svg class="sale" width="40" height="40" viewBox="0 0 40 40"><path d="M0 0h40v40z" fill="#000"/><text x="27" y="14" fill="#fff" font-size="7" font-family="Arimo,sans-serif" transform="rotate(45 27 14)" text-anchor="middle">SALE</text></svg></div>
      <div class="price">$539.00</div><div class="stars">★★★★★</div>
    </div>
    <div class="abs product" style="left:451px">
      <div class="product-photo"><div class="product-shot" role="img" aria-label="Three portable vaporizers" style="left:4px;top:16px;width:96px;background:linear-gradient(90deg,#2c2c2c,#3c6a44 60%,#2c2c2c)"></div>
        <svg class="sale" width="40" height="40" viewBox="0 0 40 40"><path d="M0 0h40v40z" fill="#000"/><text x="27" y="14" fill="#fff" font-size="7" font-family="Arimo,sans-serif" transform="rotate(45 27 14)" text-anchor="middle">SALE</text></svg></div>
      <div class="price">$199.00</div><div class="stars">★★★★<span class="off">★</span></div>
    </div>
    <div class="abs product" style="left:577px">
      <div class="product-photo"><div class="product-shot" role="img" aria-label="Handheld pen vaporizer with charger" style="background:linear-gradient(#333,#111)"></div>
        <svg class="sale" width="40" height="40" viewBox="0 0 40 40"><path d="M0 0h40v40z" fill="#000"/><text x="27" y="14" fill="#fff" font-size="7" font-family="Arimo,sans-serif" transform="rotate(45 27 14)" text-anchor="middle">SALE</text></svg></div>
      <div class="price">$135.00</div><div class="stars">★★★★<span class="off">★</span></div>
    </div>
  </section>

  <h2 class="abs section-title" style="left:76px;top:856px">Recent Blog</h2>
  <div class="abs dash" style="left:198px;top:865px;width:488px"></div>

  <article class="abs" style="left:105px;top:893px">
    <div class="author-photo" role="img" aria-label="Author portrait"></div>
  </article>
  <div class="abs" style="left:204px;top:905px">
    <div class="post-name">Marta Quenby</div>
    <p class="post-text">Lorem Ipsum is simply dummy text of the printing and typesetting industry. Lorem Ipsum has been the industry's standard dummy text ever since the 1500s, when an unknown printer took a galley of type</p>
  </div>
  <article class="abs" style="left:401px;top:893px">
    <div class="author-photo" role="img" aria-label="Author portrait"></div>
  </article>
  <div class="abs" style="left:498px;top:905px">
    <div class="post-name">Marta Quenby</div>
    <p class="post-text">Lorem Ipsum is simply dummy text of the printing and typesetting industry. Lorem Ipsum has been the industry's standard dummy text ever since the 1500s, when an unknown printer took a galley of type</p>
  </div>
</main>

<footer class="abs footer">
  <div class="abs footer-map" role="img" aria-label="Faint street map background"></div>
  <div class="abs foot-col" style="left:172px;top:41px">
    <h3>Address</h3>
    Lorem Ipsum is simply dummy<br>text of the printing and typeset-<br>ting industry<br>Phone: +1 555 010 2040<br>Email: Lorem Ipsum is simply
  </div>
  <div class="abs foot-col" style="left:361px;top:41px">
    <h3>Important Links</h3>
    Home<br>Blog<br>Marijuna 101<br>Legal Marijuna<br>Voperizers
  </div>
  <div class="abs foot-col" style="left:494px;top:41px">
    <h3>Fallow Us On</h3>
    <div class="social-row" style="margin-left:19px"><span class="sq one"></span>Linkwall</div>
    <div class="social-row" style="margin-left:19px"><span class="sq two"></span>Chirpline</div>
  </div>
  <div class="abs legal" style="left:344px;top:135px">All Rights Reserved</div>
  <div class="abs legal" style="left:617px;top:135px">Site Map | Privacy | Site Credits</div>
</footer>

</body>
</html>
```